Sports Psychology Business Card Design

Need a catchy and unique business card design for our sport psychology practice. We provide mental performance counseling and consulting to performers from all types of industries with a special emphases on athletes.The name of our practice is "Steady Core of Achievement" or "SCA" as is indicated in the logo examples submitted in this brief. Also provided were logos with specific sports referenced which represent sources of our clients from those sports.

Target Market(s)

Executives, Professionals (doctors, lawyers, etc.), Athletes, Entertainers and other performers

Contact Information for Business Card

Need to include our logo (logos provided in this brief).

Font styles to use
Other font styles liked:
• Font can be found in logo

Colors
0792cd
34a7d8
85cae6

Requirements
Must have
• Our logo and reference to our provision of mental performance counseling/consulting/coaching
Nice to have
• References to sports that our athletes play as provided in the brief.
Should not have
• This is not a general wellness consulting practice. Our focus is on consulting to improve mental performance.

```html
<!DOCTYPE html>
<html lang="en">
<head>
<meta charset="utf-8">
<title>Steady Core of Achievement – Business Card</title>
<link href="https://fonts.googleapis.com/css2?family=Montserrat:wght@400;500;600;800&display=swap" rel="stylesheet">
<style>
  :root{
    --page:#e9ebee;
    --card-dark:#15191d;
    --band-blue:#1d5e96;
    --band-text:#c9d6e2;
    --paper:#f4f5f6;
    --paper-shade:#e1e3e5;
    --brand-blue:#0a66b0;
    --brand-blue-light:#3a89c6;
    --ink:#1d2126;
    --white:#ffffff;
  }
  *{margin:0;padding:0;box-sizing:border-box}
  html,body{width:1200px;height:800px;overflow:hidden;background:var(--page);font-family:"Montserrat",Arial,sans-serif}
  .stage{position:relative;width:1200px;height:800px}
  .card{position:absolute;top:245px;width:540px;height:309px;overflow:hidden;box-shadow:0 10px 28px rgba(0,0,0,.22)}
  .card-back{left:40px;background:var(--card-dark)}
  .card-front{left:620px;background:linear-gradient(135deg,var(--paper) 0%,var(--paper-shade) 100%)}
  .tagline-band{position:absolute;left:0;right:0;top:126px;height:54px;background:var(--band-blue);display:flex;align-items:center;justify-content:center}
  .tagline{color:var(--band-text);font-weight:500;font-size:19px;letter-spacing:3px;text-transform:uppercase}
  .wave{position:absolute;inset:0}
  .brand{position:absolute;left:34px;top:160px;display:flex;align-items:center;gap:8px}
  .brand-name{font-weight:800;font-size:52px;color:var(--ink);letter-spacing:1px;line-height:1}
  .brand-dot{width:14px;height:14px;border-radius:50%;background:var(--brand-blue)}
  .contacts{position:absolute;right:34px;top:28px;list-style:none;font-size:15px;font-weight:500;color:var(--ink)}
  .contacts li{display:flex;align-items:center;gap:9px;margin-bottom:6px}
  .contacts svg{width:14px;height:14px;flex:none}
  .person{position:absolute;left:34px;bottom:26px;color:var(--white)}
  .person-name{font-weight:500;font-size:30px;letter-spacing:1.5px;text-transform:uppercase;line-height:1.1}
  .person-role{font-weight:400;font-size:12px;letter-spacing:1.2px;text-transform:uppercase;margin-top:4px}
</style>
</head>
<body>
<main class="stage">
  <section class="card card-back">
    <div class="tagline-band"><span class="tagline">The Steady Core of Achievement</span></div>
  </section>

  <section class="card card-front">
    <svg class="wave" viewBox="0 0 540 309" preserveAspectRatio="none">
      <defs>
        <linearGradient id="blueFill" x1="0" y1="1" x2="1" y2="0">
          <stop offset="0" stop-color="#0a62aa"/>
          <stop offset="1" stop-color="#3a89c6"/>
        </linearGradient>
      </defs>
      <path d="M150,230 C290,170 420,95 540,70 L540,66 C420,80 280,150 150,230 Z" fill="var(--brand-blue)"/>
      <path d="M0,240 C170,236 360,150 540,78 L540,309 L0,309 Z" fill="url(#blueFill)"/>
    </svg>

    <div class="brand"><span class="brand-name">SCA</span><span class="brand-dot"></span></div>

    <ul class="contacts">
      <li><svg viewBox="0 0 14 14"><rect x="1" y="3" width="12" height="8" fill="var(--brand-blue)"/><path d="M1,3 L7,8 L13,3" stroke="#fff" stroke-width="1.2" fill="none"/></svg>dana@steadycore.co</li>
      <li><svg viewBox="0 0 14 14"><circle cx="7" cy="7" r="6" fill="var(--brand-blue)"/><path d="M1,7 H13 M7,1 C4,4 4,10 7,13 M7,1 C10,4 10,10 7,13" stroke="#fff" stroke-width="1" fill="none"/></svg>www.steadycore.co</li>
      <li><svg viewBox="0 0 14 14"><rect x="3.5" y="1" width="7" height="12" rx="1.5" fill="none" stroke="var(--ink)" stroke-width="1.3"/><circle cx="7" cy="11" r=".8" fill="var(--ink)"/></svg>555-014-2290</li>
    </ul>

    <div class="person">
      <div class="person-name">Dana Whitlock</div>
      <div class="person-role">Mental Performance Consultant</div>
    </div>
  </section>
</main>
</body>
</html>
```